This is a book by, for and about bereaved parents and grandparents

I need a paperback size cover with front and back please...I have an example of a cover i had done myself and you will see a butterfly graphic within my Preface (My Story) which may be nice to include..or not.

Please feel free to explore your own psyche on this subject light and dark work accepted...love to see your concepts on this difficult subject.
thanks and good luck to you all!
Updates

Good Day Designer..I will post my current photo for the cover shortly and i cannot wait to see your great designs!

Apologies to you all for the delay in providing feedback ..I'm a little overwhelmed at the quality of your work and most likely will be adding a second and third place tonight when i finalize this project..thanks for your hard work and patience

thanks to all the designers for your heartfelt work on this project..it is so very personal to me and If i could afford it I'd pay you all ..do take care and thanks again for your submisions Marla .

https://www.quillnest.com/Lanterns-Along-the-Quiet-Shore-4837201956310482/?epa=SEARCH_BOX

Target Market(s)

Family of children who have died before their time especially those who've left parents and grandparents to grieve their loss of all ages.

Industry/Entity Type

Writer

Font styles to use
Serif
Sans Serif
Decorative
Script

Colors

Designer to choose colors to be used in the design.

Requirements
Must have
• feeling of loss and renewal important to end in hope and faith for future despite the years and months and days of pure agony
• my pic
• my name to be seen clearly on front of paperback
Nice to have
• maybe my butterfly graphic if it works with your concept?
• I would appreciate it if you read my Preface it 23 pages but I hope it will provide insight into the contents of the book thanks for your time and patience
Should not have
• Gravestones religous icons
• such as crosses etc

```html
<!DOCTYPE html>
<html lang="en">
<head>
<meta charset="utf-8">
<title>Lanterns Along the Quiet Shore — Paperback Cover</title>
<link href="https://fonts.googleapis.com/css2?family=Great+Vibes&family=Libre+Baskerville&family=Arimo:wght@400;700&display=swap" rel="stylesheet">
<style>
  :root {
    --page-bg: #f1efec;
    --cover-top: #8456c0;
    --cover-mid: #9466cc;
    --cover-bottom: #b08ae0;
    --ink-dark: #1e1428;
    --ink-light: #ffffff;
    --wing-pink: #f2c6e6;
    --wing-lilac: #cdb4f0;
    --wing-gold: #f6e3b8;
    --photo-tone: #a0707a;
  }
  * { margin: 0; padding: 0; box-sizing: border-box; }
  html, body {
    width: 1200px; height: 837px; overflow: hidden;
    background: var(--page-bg);
  }
  .spread { position: relative; width: 1200px; height: 837px; }
  .cover {
    position: absolute; top: 175px; width: 345px; height: 476px;
    background: linear-gradient(180deg, var(--cover-top) 0%, var(--cover-mid) 55%, var(--cover-bottom) 100%);
    overflow: hidden;
  }
  .cover--back { left: 207px; }
  .cover--front { left: 647px; }

  /* Back cover */
  .back-copy {
    position: absolute; left: 33px; top: 50px; width: 285px;
    font-family: "Arimo", Arial, sans-serif; font-size: 8.4px; line-height: 10.5px;
    color: var(--ink-dark);
  }
  .back-copy p { margin-bottom: 10.5px; }
  .author-photo {
    position: absolute; left: 24px; top: 300px; width: 64px; height: 106px;
    background: linear-gradient(180deg, #c9b9b5 0%, var(--photo-tone) 60%, #d94a8c 100%);
  }
  .author-heading {
    position: absolute; left: 103px; top: 306px;
    font-family: "Arimo", Arial, sans-serif; font-size: 17.5px; font-weight: 400;
    color: var(--ink-light); letter-spacing: 0.2px;
  }
  .author-bio {
    position: absolute; left: 100px; top: 330px; width: 230px;
    font-family: "Arimo", Arial, sans-serif; font-size: 8.4px; line-height: 10.5px;
    color: var(--ink-dark);
  }

  /* Front cover */
  .butterfly-art {
    position: absolute; left: 20px; top: 232px; width: 278px; height: 240px;
    background: radial-gradient(ellipse at 55% 55%, var(--wing-gold) 0%, var(--wing-pink) 30%, var(--wing-lilac) 55%, rgba(205,180,240,0) 75%);
    opacity: 0.9;
  }
  .title {
    position: absolute; left: 0; top: 38px; width: 100%;
    font-family: "Great Vibes", cursive; color: var(--ink-light);
    text-align: center; line-height: 1;
    text-shadow: 1px 1px 2px rgba(40, 20, 70, 0.45);
  }
  .title__small { display: block; font-size: 34px; margin-bottom: 2px; }
  .title__large { display: block; font-size: 58px; margin-bottom: 2px; }
  .subtitle {
    position: absolute; left: 0; top: 280px; width: 100%;
    font-family: "Libre Baskerville", serif; font-size: 16.5px; line-height: 22px;
    color: var(--ink-dark); text-align: center;
  }
  .byline {
    position: absolute; left: 0; top: 420px; width: 100%; text-align: center;
    font-family: "Arimo", Arial, sans-serif; color: var(--ink-dark);
  }
  .byline__by { display: block; font-size: 17px; line-height: 20px; }
  .byline__name { display: block; font-size: 17.5px; font-weight: 700; letter-spacing: 1.4px; }
</style>
</head>
<body>
<main class="spread">

  <section class="cover cover--back" aria-label="Back cover">
    <div class="back-copy">
      <p>My amazing first born son, Callum has held my hand and my heart and has shown incredible strength and fortitude after losing his precious only sister and nephew.<br>He was too young to have memories of his little brother, Jonah but I do remember it had at the time caused him great distress.</p>
      <p>His loving wife, Irene was there for me through several of my most difficult hours in South Africa on the night we arrived for Tessa and Rowan's funeral and has continued to be thoughtful throughout this journey as she, herself grieves this loss.<br>And how precious is the gift of their sweet daughter Elsie? The gratitude I feel for the joy she's brought into our lives is immeasurable. She is the beacon that guides us forward to the future.</p>
      <p>My amazing first born son, Callum has held my hand and my heart and has shown incredible strength and fortitude after losing his precious only sister and nephew.<br>He was too young to have memories of his little brother, Jonah but I do remember it had at the time caused him great distress.</p>
    </div>
    <div class="author-photo" role="img" aria-label="Portrait photograph of the author"></div>
    <h2 class="author-heading">ABOUT THE AUTHOR</h2>
    <p class="author-bio">I need a paperback size cover with front and back please...I have an example of a cover i had done myself and you will see a butterfly graphic within my Preface (My Story) which may be nice to include..or not. Please feel free to explore your own psyche on this subject light and dark work accepted...love to see your concepts on this difficult subject.</p>
  </section>

  <section class="cover cover--front" aria-label="Front cover">
    <div class="butterfly-art" role="img" aria-label="Watercolour butterfly in pink, lilac and gold with paint splashes"></div>
    <h1 class="title">
      <span class="title__small">Lanterns</span>
      <span class="title__large">Along the</span>
      <span class="title__small">Quiet</span>
      <span class="title__large">Shore</span>
    </h1>
    <p class="subtitle">Grieving the death of a child<br>in an open and healthy way</p>
    <p class="byline">
      <span class="byline__by">by</span>
      <span class="byline__name">ROSALIND HALE WHITMORE</span>
    </p>
  </section>

</main>
</body>
</html>
```